Darnell Mechanical Marketing Materials

Darnell Mechanical is a mechanical contracting company specializing in commercial and industrial piping fabrication, piping installation, HVAC and plumbing installation and service.
Piping: 35,000 square feet of shop space, 35 welding machines, 20 pioneers
Experienced project managers, draftsmen, field supervision and craftsmen knowledgeable in specific needs of industry. Certifications: ASME Section IX, the most stringent requirements in the industry and approved by the State of Ohio.

HVAC: Commercial and industrial heating, bentilating, cooling, refrigeration and controls work
24/7/365 emergency service and new installations
Diverse craftsmen abilities to solve a variety of HVAC issues
Energy saving options
Service and installation of: Boilers, Cooling Towers, Chillers, Hydronic HEating Systems, Air Compressors, Exhaust Fans, Air Andlers, Unit Heaters, Rooftop packages, Furnaces, Kitchen Equipment and much more

Plumbing: Offer diverse plumbing needs for small leaking faucet to major sewer line break. Install new or remodel plumbing and handle emergency service issues
24/7/365 service

One stop shop for all mecanical needs:
Produce large bore pipe
Produce small steel parts
Materials include copper, stailess steel, carbon steel, or whatever the job calls for
Install or service cooling or heating office or plant including chillers and cooling towers, rooftop units.
Install and service plumbing

Target Market(s)

Industrial and commercial process facilities (Power, Food and Beverage, Pharmaceutical, manufacturing).

Industry/Entity Type

Mechanical Engineering

Font styles to use
Sans Serif

Colors
0692cd
3276b5
0255a3
ffffff
9bcb3c

Requirements
Must have
• Pictures, bullets and titles - easy to read and well organized.
Nice to have
• Piping included in the design - maybe logos inside of a pipe to appear 3D.

```html
<!DOCTYPE html>
<html lang="en">
<head>
<meta charset="UTF-8">
<title>Darnell Mechanical Tri-fold Brochure</title>
<link href="https://fonts.googleapis.com/css2?family=Open+Sans:wght@400;600;700;800&family=Roboto+Condensed:wght@700&display=swap" rel="stylesheet">
<style>
  :root{
    --navy:#1c2c6b;
    --navy-deep:#15225a;
    --green:#2f9a44;
    --green-light:#8cc63f;
    --blue:#0255a3;
    --white:#ffffff;
    --ink:#3a3f4a;
    --stage:#e4e4e4;
  }
  *{box-sizing:border-box;margin:0;padding:0}
  html,body{width:1200px;height:2400px;overflow:hidden;background:var(--stage)}
  body{font-family:"Open Sans",Arial,sans-serif;color:var(--ink);position:relative}
  .spread{position:absolute;left:50px;width:1100px;height:850px;display:flex;box-shadow:0 14px 40px rgba(0,0,0,.18);background:var(--white)}
  .spread--outside{top:210px}
  .spread--inside{top:1290px;background:var(--navy);display:block}
  .panel{position:relative;width:366.66px;height:100%;overflow:hidden}
  .photo{position:absolute}
  .swoosh{position:absolute;left:0;width:100%}
  .heading-cond{font-family:"Roboto Condensed","Arial Narrow",sans-serif;font-weight:700;text-transform:uppercase}

  /* flap panel */
  .flap .photo{left:0;top:0;width:100%;height:260px;background:linear-gradient(180deg,#9fb7cc 0%,#6d8aa6 45%,#4e5b55 100%)}
  .flap .swoosh{top:220px;height:70px}
  .flap-body{position:absolute;top:300px;left:34px;right:30px;font-size:14px;line-height:1.55}
  .flap-title{color:var(--green);font-size:19px;margin:16px 0 10px;letter-spacing:.2px}
  .tick-list{list-style:none}
  .tick-list li{position:relative;padding-left:22px;margin-bottom:7px;font-size:13px;line-height:1.45}
  .tick-list li::before{content:"";position:absolute;left:0;top:3px;width:13px;height:13px;border-radius:50%;background:var(--green)}
  .tick-list li::after{content:"";position:absolute;left:4px;top:6px;width:5px;height:3px;border-left:2px solid #fff;border-bottom:2px solid #fff;transform:rotate(-45deg)}
  .band-bottom{position:absolute;left:0;bottom:0;width:100%;height:44px;background:var(--navy);color:var(--white);font-size:13px;font-weight:700;letter-spacing:.6px;display:flex;align-items:center;padding-left:30px;text-transform:uppercase}

  /* back panel */
  .back{background:linear-gradient(180deg,#34a24a 0%,#2a8c3f 100%);color:var(--white)}
  .back .swoosh{top:0;height:70px}
  .back .round-photo{position:absolute;top:28px;left:50%;margin-left:-82px;width:164px;height:164px;border-radius:50%;border:6px solid var(--white);background:radial-gradient(circle at 45% 40%,#c9cdd1 0%,#8c949b 60%,#5c646b 100%)}
  .brand{display:flex;align-items:center;gap:12px}
  .brand-dot{width:30px;height:30px;border-radius:50%;flex:none}
  .brand-name{font-weight:800;font-size:24px;line-height:1.05;text-transform:uppercase}
  .back .brand{position:absolute;top:222px;left:48px}
  .back .brand-dot{background:var(--white)}
  .back .brand-name{color:var(--white)}
  .back-text{position:absolute;top:300px;left:44px;right:40px;font-size:14.5px;line-height:1.6}
  .back-text p{margin-bottom:16px}
  .contact{position:absolute;top:520px;left:44px;font-size:15px;line-height:1.6}
  .contact-name{font-weight:700;margin-bottom:6px}
  .phone-bar{position:absolute;left:0;bottom:44px;width:100%;height:56px;background:var(--white);color:var(--navy);display:flex;align-items:center;justify-content:center;gap:10px;font-weight:800;font-size:19px}
  .phone-bar svg{width:24px;height:24px}
  .back .band-bottom{padding:0}

  /* cover panel */
  .cover .swoosh{top:0;height:180px}
  .cover .brand{position:absolute;top:38px;right:26px}
  .cover .brand-dot{background:var(--navy)}
  .cover .brand-name{color:var(--navy);font-size:25px}
  .cover .photo{left:0;top:180px;width:100%;height:380px;background:linear-gradient(180deg,#b8bec4 0%,#5e676f 50%,#2e3338 100%)}
  .service-icons{position:absolute;top:520px;left:0;width:100%;display:flex;justify-content:space-around;padding:0 24px}
  .service{display:flex;flex-direction:column;align-items:center;gap:8px}
  .service-circle{width:78px;height:78px;border-radius:50%;background:var(--green);border:4px solid var(--white);display:flex;align-items:center;justify-content:center}
  .service-circle svg{width:42px;height:42px}
  .service-label{color:var(--navy);font-size:14px}
  .cover-tagline{position:absolute;top:660px;left:0;width:100%;text-align:center;color:var(--green);font-size:28px;line-height:1.12}
  .cover .swoosh--foot{top:auto;bottom:0;height:110px}
  .web{position:absolute;bottom:16px;left:0;width:100%;text-align:center;color:var(--white);font-size:16px;letter-spacing:.3px}

  /* inside spread */
  .inside-photos{position:absolute;left:0;top:0;width:100%;height:360px;display:flex}
  .inside-photos .photo{position:relative;flex:1;height:100%}
  .photo--shop{background:linear-gradient(160deg,#8a8f92 0%,#5d6468 50%,#3d4a4e 100%)}
  .photo--crew{background:linear-gradient(180deg,#c9ced1 0%,#8d979c 55%,#485258 100%)}
  .photo--plant{background:linear-gradient(160deg,#b49a5a 0%,#7d6a3c 50%,#3f4a56 100%)}
  .inside .swoosh{top:250px;height:170px}
  .columns{position:absolute;top:380px;left:0;width:100%;display:flex}
  .column{width:366.66px;padding:0 34px;color:var(--white)}
  .column-head{display:flex;align-items:center;gap:14px;margin-bottom:20px}
  .column-head .service-circle{width:62px;height:62px;border-width:3px}
  .column-head .service-circle svg{width:32px;height:32px}
  .column-title{font-size:24px;letter-spacing:.4px}
  .dot-list{list-style:none}
  .dot-list li{position:relative;padding-left:16px;margin-bottom:9px;font-size:14px;line-height:1.5}
  .dot-list li::before{content:"";position:absolute;left:0;top:9px;width:6px;height:6px;border-radius:50%;background:var(--green-light)}
  .inside-foot{position:absolute;left:0;bottom:0;width:100%;height:70px}
  .foot-labels{position:absolute;left:0;bottom:0;width:100%;height:46px;display:flex;align-items:center;color:var(--white);font-weight:700;font-size:15px}
  .foot-labels span{width:366.66px;text-align:center}
  .foot-labels .foot-phone{display:flex;align-items:center;justify-content:center;gap:8px;font-size:17px}
  .foot-labels svg{width:20px;height:20px}
</style>
</head>
<body>

<!-- Outside spread -->
<section class="spread spread--outside">

  <div class="panel flap">
    <div class="photo" role="img" aria-label="Photo of the company's service van fleet parked in front of the shop building"></div>
    <svg class="swoosh" viewBox="0 0 367 70" preserveAspectRatio="none">
      <path d="M0 30 C120 70 250 10 367 20 L367 70 L0 70Z" fill="var(--navy)"/>
      <path d="M0 44 C120 80 250 22 367 34 L367 70 L0 70Z" fill="var(--green)"/>
      <path d="M0 54 C120 86 250 34 367 46 L367 70 L0 70Z" fill="var(--white)"/>
    </svg>
    <div class="flap-body">
      <p>Darnell Mechanical is a mechanical contracting company specializing in commercial and industrial piping fabrication, piping installation, HVAC, and plumbing installation and service.</p>
      <h3 class="flap-title heading-cond">One stop shop for all mechanical needs</h3>
      <ul class="tick-list">
        <li>Produce large bore pipe</li>
        <li>Produce small steel parts</li>
        <li>Install and service plumbing</li>
        <li>Materials include copper, stainless steel, carbon steel, or whatever the job calls for</li>
        <li>Install or service cooling or heating for office or plant, including chillers, cooling towers and rooftop units.</li>
      </ul>
    </div>
    <div class="band-bottom">Schedule your free estimate</div>
  </div>

  <div class="panel back">
    <svg class="swoosh" viewBox="0 0 367 70" preserveAspectRatio="none">
      <path d="M0 0 L367 0 L367 18 C250 40 120 8 0 30Z" fill="var(--navy)"/>
    </svg>
    <div class="round-photo" role="img" aria-label="Round photo of a stainless steel process tank with access platform"></div>
    <div class="brand"><span class="brand-dot"></span><span class="brand-name">Darnell<br>Mechanical</span></div>
    <div class="back-text">
      <p>We provide 24/7/365 service for any piping, HVAC, or plumbing emergencies.</p>
      <p>You can count on Darnell to be there at any time to handle any mechanical failure and keep your office and/or facility functioning properly.</p>
    </div>
    <div class="contact">
      <p class="contact-name">DARNELL MECHANICAL</p>
      <p>2280 HARLOW AVE.</p>
      <p>FAIRHAVEN, OH 45911</p>
      <p>PHONE: (513) 555-0142</p>
      <p>FAX: (513) 555-0187</p>
    </div>
    <div class="phone-bar">
      <svg viewBox="0 0 24 24"><circle cx="12" cy="12" r="11" fill="var(--navy)"/><path d="M8.6 6.5l1.8 0 .9 3-1.3 1c.7 1.4 1.8 2.5 3.2 3.2l1-1.3 3 .9 0 1.8c0 .6-.5 1-1.1 1C11 16.1 7.9 13 7.6 7.6c0-.6.4-1.1 1-1.1z" fill="var(--white)"/></svg>
      513-555-0142
    </div>
    <div class="band-bottom"></div>
  </div>

  <div class="panel cover">
    <svg class="swoosh" viewBox="0 0 367 180" preserveAspectRatio="none">
      <path d="M0 0 L367 0 L367 180 C250 120 120 150 0 120Z" fill="var(--navy)"/>
      <path d="M0 0 L367 0 L367 150 C250 95 120 130 0 100Z" fill="var(--green)"/>
      <path d="M0 0 L367 0 L367 140 C250 85 120 118 0 88Z" fill="var(--white)"/>
    </svg>
    <div class="brand"><span class="brand-dot"></span><span class="brand-name">Darnell<br>Mechanical</span></div>
    <div class="photo" role="img" aria-label="Photo of a rooftop cooling tower with green-painted piping"></div>
    <div class="service-icons">
      <div class="service">
        <div class="service-circle"><svg viewBox="0 0 40 40"><rect x="4" y="16" width="24" height="9" fill="#fff"/><rect x="26" y="12" width="6" height="17" fill="#fff"/><circle cx="14" cy="20.5" r="6" fill="none" stroke="#fff" stroke-width="3"/></svg></div>
        <span class="service-label heading-cond">Piping</span>
      </div>
      <div class="service">
        <div class="service-circle"><svg viewBox="0 0 40 40"><circle cx="20" cy="20" r="14" fill="none" stroke="#fff" stroke-width="3"/><path d="M20 20 L20 9 A8 8 0 0 1 27 15Z M20 20 L29 26 A8 8 0 0 1 21 30Z M20 20 L11 24 A8 8 0 0 1 13 13Z" fill="#fff"/></svg></div>
        <span class="service-label heading-cond">HVAC</span>
      </div>
      <div class="service">
        <div class="service-circle"><svg viewBox="0 0 40 40"><rect x="6" y="14" width="20" height="7" fill="#fff"/><rect x="14" y="8" width="4" height="6" fill="#fff"/><rect x="9" y="6" width="14" height="3" fill="#fff"/><path d="M22 21 L30 21 L30 30 L25 30 L25 24 L22 24Z" fill="#fff"/><circle cx="27.5" cy="34" r="2" fill="#fff"/></svg></div>
        <span class="service-label heading-cond">Plumbing</span>
      </div>
    </div>
    <h1 class="cover-tagline heading-cond">Specializing in<br>Commercial &amp; Industrial</h1>
    <svg class="swoosh swoosh--foot" viewBox="0 0 367 110" preserveAspectRatio="none">
      <path d="M0 30 C120 50 250 10 367 22 L367 110 L0 110Z" fill="var(--green)"/>
      <path d="M0 40 C120 60 250 20 367 32 L367 110 L0 110Z" fill="var(--navy)"/>
    </svg>
    <p class="web">www.darnellmechanical.com</p>
  </div>

</section>

<!-- Inside spread -->
<section class="spread spread--inside inside">
  <div class="inside-photos">
    <div class="photo photo--shop" role="img" aria-label="Photo of the fabrication shop floor with welding equipment"></div>
    <div class="photo photo--crew" role="img" aria-label="Photo of a craftsman in safety vest working on stainless steel piping"></div>
    <div class="photo photo--plant" role="img" aria-label="Photo of a process plant with stainless tanks and blue valves"></div>
  </div>
  <svg class="swoosh" viewBox="0 0 1100 170" preserveAspectRatio="none">
    <path d="M0 60 C250 20 420 140 700 70 C880 25 1000 40 1100 20 L1100 170 L0 170Z" fill="var(--green)"/>
    <path d="M0 80 C250 40 420 160 700 90 C880 45 1000 60 1100 40 L1100 170 L0 170Z" fill="var(--navy)"/>
  </svg>
  <div class="columns">
    <div class="column">
      <div class="column-head">
        <div class="service-circle"><svg viewBox="0 0 40 40"><rect x="4" y="16" width="24" height="9" fill="#fff"/><rect x="26" y="12" width="6" height="17" fill="#fff"/><circle cx="14" cy="20.5" r="6" fill="none" stroke="#fff" stroke-width="3"/></svg></div>
        <h2 class="column-title heading-cond">Piping</h2>
      </div>
      <ul class="dot-list">
        <li>35,000 square feet of shop space, 35 welding machines, 20 pioneers.</li>
        <li>Experienced project managers, draftsmen, field supervision and craftsmen knowledgeable in specific needs of industry.</li>
        <li>Certifications: ASME Section IX, the most stringent requirements in the industry and approved by the State of Ohio.</li>
      </ul>
    </div>
    <div class="column">
      <div class="column-head">
        <div class="service-circle"><svg viewBox="0 0 40 40"><circle cx="20" cy="20" r="14" fill="none" stroke="#fff" stroke-width="3"/><path d="M20 20 L20 9 A8 8 0 0 1 27 15Z M20 20 L29 26 A8 8 0 0 1 21 30Z M20 20 L11 24 A8 8 0 0 1 13 13Z" fill="#fff"/></svg></div>
        <h2 class="column-title heading-cond">HVAC</h2>
      </div>
      <ul class="dot-list">
        <li>Commercial and industrial heating, ventilating, cooling, refrigeration and controls work.</li>
        <li>24/7/365 emergency service and new installations.</li>
        <li>Diverse craftsmen abilities to solve a variety of HVAC issues.</li>
        <li>Energy saving options.</li>
        <li>Service and installation of: Boilers, Cooling Towers, Chillers, Hydronic Heating Systems, Air Compressors, Exhaust Fans, Air Handlers, Unit Heaters, Rooftop packages, Furnaces, Kitchen Equipment and much more.</li>
      </ul>
    </div>
    <div class="column">
      <div class="column-head">
        <div class="service-circle"><svg viewBox="0 0 40 40"><rect x="6" y="14" width="20" height="7" fill="#fff"/><rect x="14" y="8" width="4" height="6" fill="#fff"/><rect x="9" y="6" width="14" height="3" fill="#fff"/><path d="M22 21 L30 21 L30 30 L25 30 L25 24 L22 24Z" fill="#fff"/><circle cx="27.5" cy="34" r="2" fill="#fff"/></svg></div>
        <h2 class="column-title heading-cond">Plumbing</h2>
      </div>
      <ul class="dot-list">
        <li>Offer diverse plumbing needs for small leaking faucet to major sewer line break.</li>
        <li>Install new or remodel plumbing and handle emergency service issues.</li>
        <li>24/7/365 service.</li>
      </ul>
    </div>
  </div>
  <svg class="inside-foot" viewBox="0 0 1100 70" preserveAspectRatio="none">
    <path d="M0 24 L1100 24 L1100 70 L0 70Z" fill="var(--green)"/>
    <path d="M0 24 L1100 24 L1100 30 L0 30Z" fill="var(--white)"/>
  </svg>
  <div class="foot-labels">
    <span class="heading-cond">Schedule your free estimate</span>
    <span class="foot-phone"><svg viewBox="0 0 24 24"><circle cx="12" cy="12" r="11" fill="var(--white)"/><path d="M8.6 6.5l1.8 0 .9 3-1.3 1c.7 1.4 1.8 2.5 3.2 3.2l1-1.3 3 .9 0 1.8c0 .6-.5 1-1.1 1C11 16.1 7.9 13 7.6 7.6c0-.6.4-1.1 1-1.1z" fill="var(--green)"/></svg>513-555-0142</span>
    <span>www.darnellmechanical.com</span>
  </div>
</section>

</body>
</html>
```